International MLM Business needs Coffee Packaging Design

We are an MLM Company engaged in selling Food Supplements to our independent distributors.

We need a Packaging Design for our Instant Coffee (Cafe Latte) enhanced with Food Supplement (Ganoderma and Goji Powder)

Sachet Material is PET/AL/PE
Sachet Size is 45mm x 160mm (L x H) (FORMED)
Canvass Size is 110mm x 160mm (L x H) (FLAT)

The packaging design requirements are as follows:

1. Design must be in upright position (portrait).

2. We would like to see "VELTORIS" (our brand logo) included in the design. See uploaded file.

3. We also would like to see some "gold" touch in the label.

4. The coffee is part of our "SUPER" series.

5. Include "PREMIUM COFFEE", "WITH GANODERMA & GOJI EXTRACT" as our main selling point.

6. Add Net Weight at the lower right portion. Net Weight is 25 grams.

7. Add Serving Instruction at the Back.

1. Empty 1 sachet of VELTORIS Super Cafe Latte into a mug.
2. Fill the mug with 220ml of hot water (80 degrees celsius) and stir. (Use "80oc")
I don't know how to superscript the "o".
3. Enjoy a rich, healthy VELTORIS Super Cafe Latte.

8. Add Ingredients at the Back.

"Sugar, Non Dairy Creamer, Pure Instant Coffee, Organic Goji Extract, Organic Ganoderma Extract."

9. Add Best Before Date at the Back.

10. Add Manufacturer Details at the Back.

Our website is http://www.veltoris-example.com

*attached photo is for presentation purposes only. It's up to you to design.*

Designer Payment changed to committed. We are very serious about this project. So please kindly submit all entries. Thanks!

```html
<!DOCTYPE html>
<html lang="en">
<head>
<meta charset="utf-8">
<title>VELTORIS Super Cafe Latte – Sachet</title>
<link rel="stylesheet" href="https://fonts.googleapis.com/css2?family=Lobster&family=Patrick+Hand&family=PT+Serif&family=Roboto+Condensed:wght@400;700&display=swap">
<style>
  :root {
    --stage: #3b3b3b;
    --brown-dark: #3a1a0e;
    --brown-mid: #5a2412;
    --brown-warm: #6b2a14;
    --cocoa: #5b2c14;
    --cocoa-text: #4e2410;
    --cream-light: #f3ead7;
    --cream: #e9dcc0;
    --cream-deep: #dccaa4;
    --gold-light: #f7e08a;
    --gold: #d7a24a;
    --gold-deep: #9a5f22;
    --fold-line: rgba(150, 110, 60, 0.35);
  }
  * { box-sizing: border-box; margin: 0; padding: 0; }
  html, body {
    width: 910px; height: 1200px; overflow: hidden;
    background: var(--stage);
  }
  .sachet {
    position: absolute; left: 182px; top: 116px;
    width: 546px; height: 968px;
    background: linear-gradient(90deg, var(--cream) 0%, var(--cream-light) 45%, var(--cream) 100%);
    overflow: hidden;
    font-family: "Roboto Condensed", "Arial Narrow", sans-serif;
    color: var(--cocoa-text);
  }
  .sachet__top {
    position: absolute; left: 0; top: 0; width: 546px; height: 287px;
    background: radial-gradient(ellipse 60% 70% at 62% 30%, var(--brown-warm) 0%, var(--brown-mid) 40%, var(--brown-dark) 100%);
  }
  .gold-rule {
    position: absolute; left: 0; top: 297px; width: 546px; height: 10px;
    background: linear-gradient(90deg, var(--gold-deep), var(--gold), var(--gold-light) 55%, var(--gold) 75%, var(--brown-mid));
  }
  .gold-band {
    position: absolute; left: 0; top: 915px; width: 546px; height: 53px;
    background: linear-gradient(90deg, var(--gold) 0%, var(--gold-deep) 22%, var(--gold) 45%, var(--gold-light) 60%, var(--gold) 75%, var(--brown-mid) 100%);
  }
  .fold {
    position: absolute; left: 270px; top: 0; width: 1px; height: 968px;
    background: var(--fold-line);
  }
  .brand {
    position: absolute; left: 0; top: 118px; width: 270px;
    display: flex; flex-direction: column; align-items: center; gap: 14px;
  }
  .brand__dot {
    width: 96px; height: 96px; border-radius: 50%;
    background: var(--gold);
  }
  .brand__name {
    font-size: 30px; font-weight: 400; color: var(--gold); letter-spacing: 0.5px;
  }
  .swirl-decor {
    position: absolute; left: 150px; top: 560px; width: 300px; height: 360px;
    background: radial-gradient(ellipse at center, rgba(214, 190, 150, 0.45) 0%, rgba(214, 190, 150, 0) 70%);
  }
  .product-name {
    position: absolute; left: 0; top: 395px; width: 270px; text-align: center;
    font-family: "Lobster", cursive; font-size: 70px; line-height: 1;
    color: var(--cocoa); transform: rotate(-5deg); transform-origin: center;
    margin-top: -62px;
  }
  .tagline {
    position: absolute; left: 0; top: 434px; width: 270px; text-align: center;
    font-size: 25px; font-weight: 700; color: var(--cocoa);
  }
  .selling-point {
    position: absolute; left: 0; top: 470px; width: 270px; text-align: center;
    font-family: "Patrick Hand", cursive; font-size: 21px; line-height: 24px;
    color: #1d120a;
  }
  .cup-art {
    position: absolute; left: 87px; top: 542px; width: 164px; height: 322px;
    border-radius: 40px 40px 70px 70px;
    background: radial-gradient(ellipse at 50% 70%, rgba(110, 55, 25, 0.55) 0%, rgba(110, 55, 25, 0.15) 70%, rgba(110, 55, 25, 0) 100%);
  }
  .seal {
    position: absolute; left: 13px; top: 645px; width: 90px; height: 90px;
    border-radius: 50%;
    background: radial-gradient(circle at 40% 35%, var(--gold-light), var(--gold) 45%, var(--gold-deep) 100%);
  }
  .net-weight {
    position: absolute; right: 290px; top: 870px;
    font-size: 16px; font-weight: 700; color: var(--cocoa-text);
  }
  .net-weight strong { font-size: 25px; font-weight: 400; }
  .back {
    position: absolute; left: 297px; top: 370px; width: 240px;
  }
  .back__heading {
    font-size: 14px; font-weight: 700; text-transform: uppercase;
    padding-left: 17px; margin-bottom: 6px;
  }
  .steps { list-style: none; }
  .step {
    display: flex; gap: 6px; font-size: 13.5px; font-weight: 700;
    line-height: 18px; margin-bottom: 12px;
  }
  .step__num {
    flex: 0 0 18px; height: 18px; border-radius: 50%;
    background: #3c1c0c; color: var(--cream-light);
    font-size: 12px; text-align: center; line-height: 18px; margin-top: 4px;
  }
  .ingredients {
    padding-left: 17px; font-size: 13.5px; font-weight: 700; line-height: 20.5px;
    margin-top: -4px;
  }
  .method-art {
    display: flex; gap: 20px; margin: 26px 0 0 15px;
  }
  .method-art__item {
    width: 44px; height: 48px; border-radius: 4px 4px 22px 22px;
    background: linear-gradient(180deg, rgba(90, 60, 40, 0.08), rgba(90, 60, 40, 0.3));
  }
  .best-before {
    margin: 44px 0 0 17px; font-family: "PT Serif", Georgia, serif;
    font-size: 15.5px; line-height: 21px;
  }
  .maker { margin: 24px 0 0 17px; }
  .maker__label { font-size: 14px; font-weight: 700; }
  .maker__name { font-size: 21.5px; font-weight: 700; margin-top: 2px; }
  .maker__web { font-size: 15px; font-weight: 700; letter-spacing: 2.5px; margin-top: 4px; }
</style>
</head>
<body>
  <main class="sachet">
    <div class="sachet__top"></div>
    <div class="gold-rule"></div>
    <div class="gold-band"></div>
    <div class="fold"></div>

    <div class="brand">
      <span class="brand__dot"></span>
      <span class="brand__name">veltoris-example</span>
    </div>

    <div class="swirl-decor" role="img" aria-label="Faint cream steam swirl decoration"></div>

    <h1 class="product-name">Cafe Latte</h1>
    <p class="tagline">PREMIUM COFFEE</p>
    <p class="selling-point">with ganoderma<br>&amp; goji extract</p>

    <div class="cup-art" role="img" aria-label="Brown coffee cup illustration with rising steam swirl"></div>
    <div class="seal" role="img" aria-label="Gold premium coffee seal"></div>

    <p class="net-weight">Net W <strong>25</strong> gms.</p>

    <section class="back">
      <h2 class="back__heading">Serving Instruction</h2>
      <ol class="steps">
        <li class="step"><span class="step__num">1</span><span>Empty 1 sachet of VELTORIS<br>Super Cafe Latte into a mug.</span></li>
        <li class="step"><span class="step__num">2</span><span>Fill the mug with 220ml of hot<br>water (80 degrees celsius)</span></li>
        <li class="step"><span class="step__num">3</span><span>Enjoy a rich, healthy<br>VELTORIS Super Cafe Latte.</span></li>
      </ol>
      <h2 class="back__heading">Ingredients</h2>
      <p class="ingredients">"Sugar, Non Dairy Creamer,<br>Pure Instant Coffee, Organic Goji<br>Extract, Organic Ganoderma Extract."</p>

      <div class="method-art">
        <div class="method-art__item" role="img" aria-label="Pouring sachet into mug"></div>
        <div class="method-art__item" role="img" aria-label="Adding hot water to mug"></div>
        <div class="method-art__item" role="img" aria-label="Stirring the mug"></div>
      </div>

      <p class="best-before">Best before Dec 2015<br>Best before Dec 2015</p>

      <div class="maker">
        <p class="maker__label">Manufacturer by:</p>
        <p class="maker__name">Companey Name Here</p>
        <p class="maker__web">www.veltoris-example.com</p>
      </div>
    </section>
  </main>
</body>
</html>
```